Stationery Design Project - Tarnwell Corporate

Business Cards
Size: 90mm x 55mm
Letterhead
Size: A4 - 210mm x 297mm
With Compliments Slip
Size: DL - 210mm x 99mm
Presentation Folder
Size: A4

Tarnwell Corporate
website: www.tarnwellcorporate.com.au (Under construction)
Offices: *Perth *Brisbane * Seoul

A company that supply Safety consultantcy services

```html
<!DOCTYPE html>
<html lang="en">
<head>
<meta charset="utf-8">
<title>Tarnwell Corporate – Business Cards</title>
<link rel="stylesheet" href="https://fonts.googleapis.com/css2?family=Mulish:wght@300;400;700;800&display=swap">
<style>
  :root {
    --board: #aeadb2;
    --card: #ffffff;
    --brand-blue: #1b6fb3;
    --band-blue: #1d69ad;
    --logo-grey: #8fa6b4;
    --mark-blue: #3a8fc8;
    --text-grey: #5b5e62;
    --deco-grey: rgba(205, 214, 222, 0.85);
    --deco-blue: rgba(196, 222, 240, 0.9);
  }
  * { margin: 0; padding: 0; box-sizing: border-box; }
  html, body { width: 1200px; height: 848px; overflow: hidden; }
  body {
    background: var(--board);
    font-family: "Mulish", Arial, sans-serif;
    position: relative;
  }
  .card {
    position: absolute;
    width: 365px;
    height: 221px;
    background: var(--card);
    overflow: hidden;
    box-shadow: 0 2px 4px rgba(0, 0, 0, 0.18);
  }
  .card--front-a { left: 204px; top: 174px; }
  .card--back-a  { left: 637px; top: 174px; }
  .card--front-b { left: 204px; top: 447px; }
  .card--back-b  { left: 637px; top: 447px; }

  .card__band {
    position: absolute;
    left: 0; right: 0; bottom: 0;
    height: 9px;
    background: var(--band-blue);
  }

  .brand {
    position: absolute;
    display: flex;
    align-items: center;
    gap: 5px;
  }
  .brand__square {
    flex: none;
    width: 34px; height: 34px;
    background: var(--mark-blue);
  }
  .brand__name {
    font-weight: 300;
    font-size: 18px;
    letter-spacing: 0.4px;
    color: var(--logo-grey);
    white-space: nowrap;
  }
  .card--front-a .brand,
  .card--front-b .brand { left: 70px; top: 86px; }
  .card--back-a .brand  { left: 150px; top: 19px; }
  .card--back-b .brand  { left: 20px; top: 19px; }
  .card--back-a .brand__square,
  .card--back-b .brand__square { width: 30px; height: 30px; }
  .card--back-a .brand__name,
  .card--back-b .brand__name { font-size: 16px; }

  .web-address {
    position: absolute;
    left: 0; right: 0;
    top: 189px;
    text-align: center;
    font-size: 10px;
    color: var(--brand-blue);
  }
  .web-address strong { font-weight: 800; }

  .decoration { position: absolute; }
  .card--back-a .decoration {
    left: 0; top: 47px; width: 185px; height: 165px;
    background:
      radial-gradient(ellipse at 35% 65%, var(--deco-blue) 0%, var(--deco-grey) 40%, rgba(255,255,255,0) 72%);
  }
  .card--back-b .decoration {
    left: 161px; top: 44px; width: 204px; height: 168px;
    background:
      radial-gradient(ellipse at 60% 60%, var(--deco-blue) 0%, var(--deco-grey) 40%, rgba(255,255,255,0) 72%);
  }

  .person {
    position: absolute;
    text-align: center;
    width: 160px;
  }
  .card--back-a .person { left: 17px; top: 100px; }
  .card--back-b .person { left: 201px; top: 97px; }
  .person__name {
    font-weight: 800;
    font-size: 9.5px;
    color: var(--brand-blue);
    line-height: 1.25;
  }
  .person__role {
    font-size: 9.5px;
    color: var(--text-grey);
    line-height: 1.25;
  }

  .contact {
    position: absolute;
    top: 157px;
    font-size: 9px;
    line-height: 12px;
    color: var(--text-grey);
    list-style: none;
    white-space: nowrap;
  }
  .card--back-a .contact { right: 18px; text-align: right; }
  .card--back-b .contact { left: 21px; text-align: left; }
</style>
</head>
<body>

  <section class="card card--front-a">
    <div class="brand">
      <span class="brand__square"></span>
      <span class="brand__name">Tarnwell Corporate</span>
    </div>
    <p class="web-address">www.<strong>tarnwellcorporate</strong>.com.au</p>
    <div class="card__band"></div>
  </section>

  <section class="card card--back-a">
    <div class="decoration" role="img" aria-label="Soft grey and blue stacked-block graphic"></div>
    <div class="brand">
      <span class="brand__square"></span>
      <span class="brand__name">Tarnwell Corporate</span>
    </div>
    <div class="person">
      <p class="person__name">Nombre Apellido Apellido</p>
      <p class="person__role">Cargo</p>
    </div>
    <ul class="contact">
      <li>471-2050 / 990004318</li>
      <li>info@tarnwellcorporate.com</li>
      <li>www.tarnwellcorporate.com.au</li>
      <li>23, Kestrel Way - 6000 Perth WA</li>
    </ul>
    <div class="card__band"></div>
  </section>

  <section class="card card--front-b">
    <div class="brand">
      <span class="brand__square"></span>
      <span class="brand__name">Tarnwell Corporate</span>
    </div>
    <p class="web-address">www.<strong>tarnwellcorporate</strong>.com.au</p>
    <div class="card__band"></div>
  </section>

  <section class="card card--back-b">
    <div class="decoration" role="img" aria-label="Soft grey and blue stacked-block graphic"></div>
    <div class="brand">
      <span class="brand__square"></span>
      <span class="brand__name">Tarnwell Corporate</span>
    </div>
    <div class="person">
      <p class="person__name">Nombre Apellido Apellido</p>
      <p class="person__role">Cargo</p>
    </div>
    <ul class="contact">
      <li>471-2050 / 990004318</li>
      <li>info@tarnwellcorporate.com</li>
      <li>www.tarnwellcorporate.com.au</li>
      <li>23, Kestrel Way - 6000 Perth WA</li>
    </ul>
    <div class="card__band"></div>
  </section>

</body>
</html>
```